Design a Small Graphic for a client brochure and Website

We need a a fairly simple diagram/graphic to replace the existing graphic in our brochures and website. We are a Private Wealth Advice firm, dealing with high-end clients. We would like to be able to copyright the final design. We need this design to be stylish and have a long shelf-life.
The original design is quite old and was not updated to reflect our company growth or changes in our website design and brochure designs.
Updates

Target Market(s)

Private Wealth clients
High end
Age 45 plus

Industry/Entity Type

Finance

Font styles to use
Sans Serif
Other font styles liked:
• Stag Sans

Requirements
Must have
• Corporate colours only - plus white
• Pantone 288c (Blue)
• Pantone Cool grey 10c
• Pantone 666c (purple - only limited use for highlighting etc)
• Corporate fonts only
• Stag Sans light, book and thin
• Must provide AI editable files
• Must be able to scale to size and remove/replace any text
• Must be in keeping with our brochures and website which can be viewed at www.ridgefold-advisory.com.au
Nice to have
• We want something more vibrant than the image we are using. Something which is in keeping with our image but that is really eye catching.

```html
<!DOCTYPE html>
<html lang="en">
<head>
<meta charset="utf-8">
<title>Family Wealth Cycle</title>
<link href="https://fonts.googleapis.com/css2?family=Arimo:wght@400;700&family=Roboto+Condensed:wght@400;500&display=swap" rel="stylesheet">
<style>
  :root {
    --blue: #0033c4;
    --grey: #76858b;
    --lilac: #a3aaee;
    --white: #ffffff;
    --ink: #111111;
    --ring-light: #a7a9e6;
    --ring-dark: #676569;
    --edge: #9aa0a4;
  }
  html, body {
    margin: 0;
    padding: 0;
    width: 1200px;
    height: 1174px;
    overflow: hidden;
    background: var(--white);
  }
  .cycle-diagram { display: block; width: 1200px; height: 1174px; }
  .ring-light { fill: none; stroke: var(--ring-light); stroke-width: 14; stroke-linecap: round; }
  .ring-dark { fill: none; stroke: var(--ring-dark); stroke-width: 14; stroke-linecap: round; }
  .head-light { fill: var(--ring-light); }
  .head-dark { fill: var(--ring-dark); }
  .piece { stroke: var(--white); stroke-width: 8; stroke-linejoin: round; }
  .piece-purpose { fill: var(--blue); }
  .piece-wealth { fill: var(--grey); }
  .piece-investment { fill: var(--lilac); }
  .piece-legacy { fill: var(--white); stroke: var(--edge); stroke-width: 3; }
  .knob { stroke: var(--white); stroke-width: 6; }
  .knob-blue { fill: var(--blue); }
  .knob-grey { fill: var(--grey); }
  .knob-lilac { fill: var(--lilac); }
  .knob-white { fill: var(--white); stroke: var(--edge); stroke-width: 3; }
  .hub { fill: var(--white); }
  .label {
    font-family: "Roboto Condensed", "Arial Narrow", sans-serif;
    font-size: 92px;
    fill: var(--ink);
    text-anchor: middle;
  }
  .label-purpose {
    font-family: "Arimo", Arial, sans-serif;
    font-size: 88px;
    fill: var(--white);
    text-anchor: middle;
  }
  .step {
    font-family: "Arimo", Arial, sans-serif;
    font-weight: 700;
    font-size: 90px;
    text-anchor: middle;
  }
  .step-light { fill: var(--white); font-weight: 400; }
  .step-dark { fill: var(--ink); }
</style>
</head>
<body>
<svg class="cycle-diagram" viewBox="0 0 1400 1370" xmlns="http://www.w3.org/2000/svg" role="img" aria-label="Four-step cycle: Purpose, Wealth Planning, Investment Planning, Your Legacy, around Your Family">
  <g class="cycle-arrows">
    <path class="ring-light" d="M208 1162 A690 690 0 0 1 1037 83"/>
    <polygon class="head-light" points="1155,212 1025,35 1035,100 958,130"/>
    <path class="ring-dark" d="M1201 204 A690 690 0 0 1 389 1301"/>
    <polygon class="head-dark" points="250,1165 360,1322 372,1262 432,1238"/>
  </g>

  <g class="puzzle">
    <path class="piece piece-purpose" d="M168 692 A545 545 0 0 1 713 147 L713 520 A172 172 0 0 0 541 692 Z"/>
    <path class="piece piece-wealth" d="M713 147 A545 545 0 0 1 1258 692 L885 692 A172 172 0 0 0 713 520 Z"/>
    <path class="piece piece-investment" d="M1258 692 A545 545 0 0 1 713 1237 L713 864 A172 172 0 0 0 885 692 Z"/>
    <path class="piece piece-legacy" d="M713 1237 A545 545 0 0 1 168 692 L541 692 A172 172 0 0 0 713 864 Z"/>

    <circle class="knob knob-grey" cx="662" cy="335" r="34"/>
    <rect class="knob-grey" x="690" y="318" width="26" height="34"/>
    <circle class="knob knob-lilac" cx="1072" cy="634" r="34"/>
    <rect class="knob-lilac" x="1055" y="662" width="34" height="28"/>
    <circle class="knob knob-white" cx="762" cy="1050" r="34"/>
    <rect fill="var(--white)" x="712" y="1033" width="26" height="34"/>
    <circle class="knob knob-blue" cx="355" cy="742" r="34"/>
    <rect class="knob-blue" x="338" y="692" width="34" height="26"/>

    <circle class="hub" cx="713" cy="692" r="168"/>
  </g>

  <g class="labels">
    <text class="label-purpose" x="462" y="455">Purpose</text>
    <text class="label" x="962" y="433">Wealth</text>
    <text class="label" x="962" y="510">Planning</text>
    <text class="label" x="942" y="933">Investment</text>
    <text class="label" x="942" y="1012">Planning</text>
    <text class="label" x="470" y="922">Your</text>
    <text class="label" x="470" y="1000">Legacy</text>
    <text class="label" x="710" y="683">Your</text>
    <text class="label" x="710" y="760">Family</text>
  </g>

  <g class="steps">
    <text class="step step-light" x="660" y="255">1</text>
    <text class="step step-light" x="1208" y="668">2</text>
    <text class="step step-dark" x="757" y="1200">3</text>
    <text class="step step-dark" x="215" y="788">4</text>
  </g>
</svg>
</body>
</html>
```